Healthcare IT company looking for business card design

We develop IT systems for healthcare that significantly reduces cost and improves quality.

We want a business card design that is professional and clean, and using the colors in our logo.

Target Market(s)

Doctors and decision makers in the healthcare industry

Industry/Entity Type

Healthcare

Contact Information for Business Card

It should include
Name and title, address, telephone

Tobias Vrenholt, CEO
+46 712 418257
tobias@kelvaro.se

Font styles to use
Serif

Colors
0355a3
ed282f

Requirements
Must have
• Clean design
• Professional feel
Nice to have
• N/A
Should not have
• N/A

```html
<!DOCTYPE html>
<html lang="en">
<head>
<meta charset="utf-8">
<title>Kelvaro Business Card</title>
<link href="https://fonts.googleapis.com/css2?family=Cormorant+SC:wght@600&family=Carlito:wght@400;700&display=swap" rel="stylesheet">
<style>
  :root {
    --brand-blue: #0355a3;
    --brand-red: #ed282f;
    --card-white: #ffffff;
    --backdrop: #e9e9ec;
    --ink: #1a1a1a;
  }
  html, body {
    margin: 0;
    padding: 0;
    width: 1200px;
    height: 1200px;
    overflow: hidden;
    background: var(--backdrop);
  }
  .canvas {
    position: relative;
    width: 1200px;
    height: 1200px;
  }
  .card {
    position: absolute;
    left: 200px;
    width: 800px;
    height: 457px;
    box-shadow: 0 6px 18px rgba(0,0,0,0.18);
    overflow: hidden;
  }
  .card-front {
    top: 110px;
    background: var(--card-white);
    display: flex;
    align-items: center;
    justify-content: center;
  }
  .wordmark {
    font-family: "Carlito", "Calibri", sans-serif;
    font-weight: 700;
    font-size: 128px;
    color: var(--brand-blue);
    letter-spacing: 1px;
    margin: 0;
  }
  .card-back {
    top: 633px;
  }
  .back-decoration {
    position: absolute;
    inset: 0;
    background: linear-gradient(90deg, var(--brand-blue) 0%, var(--brand-red) 50%, var(--brand-blue) 100%);
  }
  .contact-panel {
    position: absolute;
    left: 250px;
    top: 128px;
    width: 300px;
    height: 200px;
    background: var(--card-white);
    display: flex;
    flex-direction: column;
    align-items: center;
    justify-content: center;
    text-align: center;
  }
  .contact-name {
    font-family: "Cormorant SC", "Times New Roman", serif;
    font-weight: 600;
    font-size: 25px;
    color: var(--brand-red);
    margin: 0 0 6px;
    white-space: nowrap;
  }
  .contact-title {
    font-family: "Carlito", "Calibri", sans-serif;
    font-size: 17px;
    color: var(--ink);
    margin: 0 0 10px;
  }
  .contact-line {
    font-family: "Carlito", "Calibri", sans-serif;
    font-size: 18px;
    color: var(--ink);
    margin: 0 0 2px;
    white-space: nowrap;
  }
  .contact-label {
    color: var(--brand-red);
    font-weight: 700;
  }
</style>
</head>
<body>
<div class="canvas">
  <section class="card card-front">
    <h1 class="wordmark">Kelvaro</h1>
  </section>

  <section class="card card-back">
    <div class="back-decoration" role="img" aria-label="Decorative brand graphic in blue and red"></div>
    <div class="contact-panel">
      <p class="contact-name">Tobias Vrenholt</p>
      <p class="contact-title">CEO</p>
      <p class="contact-line">[<span class="contact-label">P</span>] +46 712 418257</p>
      <p class="contact-line">[<span class="contact-label">E</span>] tobias@kelvaro.se</p>
    </div>
  </section>
</div>
</body>
</html>
```